Simple 3 page web design project

This is a simple 3 or 4 page site that is very straight forward.

I have a furnished apartment to lease, and wish to design a clean 3 or 4 page website to advertise the apartment. I am thinking a clean black background with a nice image of the inside of the apartment in the center of the page.

I have attached a rough mockup I did to show what I was thinking of.

Also, room for a nice title and some text above the large picture. At the bottom or on the side, there should be thumbnails that can be clicked to view other images of the apartment with labels below each one.

A menu "Home", "how to rent", and "contact" should be included, as well as a map of where the apartment is on the last page.

I prefer the project be written in HTML5.

I will provide the address and the pictures when I decide on a provider.

I have attached a sample website mock up I did in photoshop to give you an idea of what I am looking for.

Target Market(s)

business travelers and families needing temporary homes

Industry/Entity Type

Apartment

Requirements
Must have
• Should be written in HTML5
Must be able to upload and resize images using thumbnails
must have a contact form
must have the address on a google map on one of the pages
Must have normal items to optomize google search, such as title page, title, etc.
Should not have
• No add-in modules that will have to be kept up. The site shold be written in HTML

```html
<!DOCTYPE html>
<html lang="en">
<head>
<meta charset="utf-8">
<title>Bayou Crest, LLC Properties – Furnished Executive Apartment in Mobile, Alabama</title>
<link href="https://fonts.googleapis.com/css2?family=Oswald:wght@500;600&family=Open+Sans:ital,wght@0,400;0,700;1,400&display=swap" rel="stylesheet">
<style>
:root{
  --bg-dark:#141414;
  --panel:#262626;
  --panel-edge:#3c3c3c;
  --gold:#f5a90f;
  --gold-light:#ffd35a;
  --text-light:#e8e8e8;
  --text-muted:#8c8c8c;
  --blind-teal:#7fb3bd;
  --wall-white:#eef1f2;
  --sofa-black:#1c1c1e;
}
*{margin:0;padding:0;box-sizing:border-box}
html,body{width:1084px;height:1200px;overflow:hidden}
body{position:relative;background:var(--bg-dark);font-family:"Open Sans",Arial,sans-serif;color:var(--text-light)}
.backdrop{position:absolute;inset:0;background:
  linear-gradient(180deg,rgba(0,0,0,0) 0%,rgba(0,0,0,.55) 100%),
  radial-gradient(ellipse at 50% 45%,#4a4a4a 0%,#2c2c2c 50%,#111 100%)}
.brand{position:absolute;left:24px;top:36px}
.brand-name{font-family:"Oswald",Arial,sans-serif;font-weight:600;font-size:34px;letter-spacing:1.5px;color:var(--gold);line-height:1.1}
.brand-tagline{font-family:"Oswald",Arial,sans-serif;font-weight:500;font-size:18.5px;letter-spacing:1.2px;color:#bdbdbd;margin-top:5px}
.main-nav{position:absolute;top:59px;left:0;width:100%;height:60px}
.nav-item{position:absolute;height:45px;border-radius:5px;background:linear-gradient(#5a5a5a,#333);border:1px solid #222;
  font-size:18px;letter-spacing:1px;color:#fff;display:flex;align-items:center;justify-content:center;text-decoration:none}
.nav-item::after{content:"";position:absolute;bottom:-10px;left:50%;margin-left:-10px;border:10px solid transparent;border-bottom:0;border-top-color:#333}
.nav-item.active{background:linear-gradient(var(--gold-light),var(--gold));color:#222}
.nav-item.active::after{border-top-color:var(--gold)}
.gallery{position:absolute;left:13px;top:137px;width:1047px;height:666px;background:#050505;border-radius:6px;box-shadow:0 0 14px #000}
.feature-photo{position:absolute;left:11px;top:11px;width:1025px;height:644px;background:
  linear-gradient(180deg,rgba(28,28,30,0) 50%,rgba(28,28,30,.55) 72%,rgba(230,230,230,.6) 90%),
  linear-gradient(90deg,var(--blind-teal) 0%,#a9cbd1 25%,#d6e3e6 38%,var(--blind-teal) 50%,#cfdee1 58%,var(--wall-white) 70%,#dfe4e6 100%)}
.thumb-strip{position:absolute;left:810px;top:11px;width:226px;height:644px;background:linear-gradient(120deg,rgba(90,90,90,.75),rgba(40,40,40,.8))}
.thumb-strip svg{position:absolute;inset:0}
.section-tab{position:absolute;left:36px;top:828px;width:336px;height:46px;background:var(--panel);border:1px solid var(--panel-edge);border-bottom:0;border-radius:4px 4px 0 0;
  padding:11px 18px;font-style:italic;font-weight:400;font-size:17.5px;color:var(--gold)}
.about-panel{position:absolute;left:13px;top:874px;width:1047px;height:129px;background:var(--panel);border:1px solid var(--panel-edge);border-radius:5px;
  padding:12px 32px;font-style:italic;font-size:17.5px;line-height:32.5px;color:var(--text-light);white-space:nowrap}
.read-more{position:absolute;left:935px;top:1003px;width:98px;height:25px;background:#3a3a3a;border-radius:0 0 4px 4px;font-style:italic;font-weight:700;
  font-size:11px;letter-spacing:1px;color:var(--text-muted);text-align:center;line-height:25px;text-decoration:none}
.copyright{position:absolute;left:13px;top:1063px;font-size:13px;font-weight:700;color:var(--text-muted)}
.social{position:absolute;left:914px;top:1064px;display:flex;gap:21px}
.social span{width:20px;height:20px;border-radius:50%;background:#d8d8d8}
.social span:first-child{background:var(--gold)}
</style>
</head>
<body>
<div class="backdrop" role="img" aria-label="Dimmed photograph of the furnished living room as page background"></div>

<header class="brand">
  <h1 class="brand-name">BAYOU CREST, LLC PROPERTIES</h1>
  <p class="brand-tagline">FURNISHED EXECUTIVE APARTMENT IN MOBILE, ALABAMA</p>
</header>

<nav class="main-nav">
  <a class="nav-item active" href="#" style="left:624px;width:88px">HOME</a>
  <a class="nav-item" href="#" style="left:733px;width:174px">HOW TO RENT</a>
  <a class="nav-item" href="#" style="left:929px;width:131px">CONTACT</a>
</nav>

<section class="gallery">
  <div class="feature-photo" role="img" aria-label="Living room: black sofa under two windows with teal patterned blinds, round white table with a white orchid, dark rug and a floor lamp"></div>
  <div class="thumb-strip">
    <svg width="226" height="644" viewBox="0 0 226 644">
      <defs>
        <radialGradient id="thumb-grey" cx="50%" cy="40%" r="60%">
          <stop offset="0" stop-color="#d0d0d0"/><stop offset=".6" stop-color="#8a8a8a"/><stop offset="1" stop-color="#4a4a4a"/>
        </radialGradient>
        <linearGradient id="thumb-active" x1="0" y1="0" x2="0" y2="1">
          <stop offset="0" stop-color="#8fbcc5"/><stop offset=".45" stop-color="#e9eeef"/><stop offset=".75" stop-color="#2a2a2c"/><stop offset="1" stop-color="#dcdcdc"/>
        </linearGradient>
      </defs>
      <polyline points="107,16 117,10 127,16" fill="none" stroke="#aaa" stroke-width="3"/>
      <polyline points="107,624 117,630 127,624" fill="none" stroke="#aaa" stroke-width="3"/>
      <g stroke="#c8c8c8" stroke-width="4" fill="url(#thumb-grey)">
        <circle cx="117" cy="108" r="68" role="img" aria-label="Living room with sofa"/>
        <circle cx="117" cy="206" r="68" role="img" aria-label="Bedroom"/>
        <circle cx="117" cy="534" r="68" role="img" aria-label="Lounge corner"/>
        <circle cx="117" cy="457" r="68" role="img" aria-label="Dining area"/>
        <circle cx="117" cy="381" r="68" role="img" aria-label="Kitchen"/>
      </g>
      <path d="M48,265 L36,275 L48,285" fill="#eee" stroke="#f5a90f" stroke-width="4"/>
      <circle cx="120" cy="275" r="74" fill="url(#thumb-active)" stroke="#f5a90f" stroke-width="5" role="img" aria-label="Selected: main living room"/>
    </svg>
  </div>
</section>

<h2 class="section-tab">ABOUT THE FURNISHED APARTMENT</h2>
<section class="about-panel">
  <p>This apartment is both newly renovated and furnished with all Cozy-Rest furniture to ensure the most<br>comfortable enviorment possible. Located in desireable Mid-Town Mobile, Alabama, the apartment is located ony miles<br>from downtown as well as shopping.</p>
</section>
<a class="read-more" href="#">Read More...</a>

<footer>
  <p class="copyright">© 2013 BAYOU CREST, LLC Properties. All Rights Reserved.</p>
  <div class="social"><span></span><span></span><span></span><span></span></div>
</footer>
</body>
</html>
```